Flyer-Design für psychologische Beratung und Therapie
Zielgruppe
In meiner Praxis für psychologische Beratung und Therapie unterstütze ich Menschen dabei, ihre Probleme zu lösen. Schwerpunkte sind die Stärkung des Selbstwertgefühls, Überwindung von Ängsten und Krisen.
Aufgabenstellung
Din lang 4-Seitig
(Zitat)
'Bei aller Ernsthaftigkeit und Empathie dürfen Leichtigkeit,
Zuversicht und Humor in der Therapie nicht zu kurz kommen.“
(Text)
Mein Name ist Karl Ewald Lambrecht, ich bin Transaktionsanalytiker, psychotherapeutischer Heilpraktiker und begeisterter VKT® Therapeut. Wenn Sie zufriedener leben wollen, neue Wege einschlagen oder sich beruflich oder persönlich weiterentwickeln wollen, begleite ich Sie gern dabei!
Möchten Sie ein stärkeres Selbstwertgefühl entwickeln, Ängste reduzieren oder eine akute Krise überwinden? Oder geeignete Strategien entwickeln, damit Sie Ihren Beruf zufriedener und erfolgreicher ausüben können? Auf dem Weg zu Ihrem Ziel biete ich Ihnen Unterstützung, vereinbaren Sie gerne einen ersten Termin!

```html
<!DOCTYPE html>
<html lang="de">
<head>
<meta charset="utf-8">
<title>Flyer DIN lang – Psychologische Beratung & Therapie</title>
<link href="https://fonts.googleapis.com/css2?family=Jost:ital,wght@0,300;0,400;0,500;1,400&display=swap" rel="stylesheet">
<style>
  :root{
    --orange:#f39a1e;
    --grey:#7b7b7b;
    --grey-dark:#5e5e5e;
    --grey-light:#d6d6d6;
    --label:#8a8a8a;
    --white:#ffffff;
  }
  *{box-sizing:border-box;margin:0;padding:0}
  html,body{width:1200px;height:656px;overflow:hidden;background:var(--white)}
  body{position:relative;font-family:"Jost",sans-serif;color:var(--grey-dark)}
  .panel{position:absolute;top:70px;width:241px;height:480px;border:1px solid var(--grey-light);overflow:hidden;background:var(--white)}
  .panel--back{left:73px}
  .panel--cover{left:314px}
  .panel--inner-left{left:646px}
  .panel--inner-right{left:886px}
  .abs{position:absolute}
  .panel-label{position:absolute;top:580px;width:241px;text-align:center;font-weight:300;font-size:21px;color:var(--label)}

  /* Rückseite */
  .back-title{left:32px;top:24px;font-size:17px;font-weight:400;color:var(--grey-dark)}
  .back-intro{left:32px;top:61px;width:200px;font-size:7.8px;line-height:13px;color:var(--orange);font-weight:500}
  .back-subtitle{left:32px;top:152px;font-size:10.5px;line-height:14.5px;color:var(--grey-dark)}
  .benefits{left:32px;top:195px;width:205px;list-style:none;font-size:7.8px;line-height:13px;color:var(--orange);font-weight:500}
  .benefits li{position:relative;margin-bottom:4.5px}
  .benefits li::before{content:"•";position:absolute;left:-10px}
  .back-shape{left:0;top:0}
  .contact-title{left:32px;top:362px;font-size:16px;font-weight:500;color:var(--grey)}
  .contact{color:var(--white);font-size:7.8px;line-height:13px}
  .contact-address{left:33px;top:395px}
  .contact-phone{left:141px;top:395px}
  .contact-mail{left:141px;top:421px}
  .contact-hours{left:67px;top:446px}
  .contact-icon{position:absolute}

  /* Cover */
  .brand-dot{left:24px;top:25px;width:28px;height:28px;border-radius:50%;background:var(--orange)}
  .brand-name{left:66px;top:24px;font-size:13.5px;letter-spacing:.4px;font-weight:400;color:var(--grey);white-space:nowrap}
  .brand-tagline{left:66px;top:43px;font-size:9.4px;font-weight:300;color:var(--orange);white-space:nowrap}
  .cover-art{left:0;top:0}

  /* Innenteil links */
  .portrait{left:0;top:0}
  .quote{right:22px;top:138px;width:200px;text-align:right;font-style:italic;font-size:9.8px;line-height:14.5px;color:var(--grey-dark)}
  .intro-bar{left:28px;top:229px;width:3px;height:34px;background:var(--orange)}
  .intro-text{left:42px;top:224px;width:186px;font-size:7.8px;line-height:15.1px;color:var(--orange);font-weight:500}

  /* Innenteil rechts */
  .services-title{left:26px;top:24px;font-size:17px;line-height:20.5px;color:var(--grey-dark)}
  .service{position:absolute;left:0;width:241px;text-align:center}
  .service-icon{display:block;margin:0 auto}
  .service-name{font-size:10px;color:var(--grey);margin-top:8px}
  .service-text{font-size:7.8px;line-height:14.5px;color:var(--orange);font-weight:500;margin-top:4px}
</style>
</head>
<body>

<!-- Rückseite -->
<section class="panel panel--back">
  <h2 class="abs back-title">Ich freue mich auf Sie!</h2>
  <p class="abs back-intro">In meiner Privatpraxis können Sie zeitnah Termine vereinbaren. Gesetzliche Krankenversicherungen übernehmen die Kosten in der Regel nicht, Privatversicherte sollten sich vorher bei Ihrem Anbieter erkundigen, inwieweit die Kosten der Behandlung übernommen werden.</p>
  <h3 class="abs back-subtitle" style="font-weight:400">Als Selbstzahler haben Sie jedoch<br>zahlreiche Vorteile:</h3>
  <ul class="abs benefits">
    <li>Keine Wartezeit, Sie bekommen kurzfristig Termine.</li>
    <li>Sie genießen den Vorteil der absoluten Diskretion, es entfällt die Beantragung der Kostenerstattung und somit eine Dokumentation bei Ihrer Krankenkasse.</li>
    <li>Sie sind nicht an eine bestimmt Frequenz oder bestimmte Anzahl von Therapiestunden gebunden.</li>
    <li>Die Kosten können Sie i.d.R. steuerlich<br>geltend machen.</li>
  </ul>
  <svg class="abs back-shape" width="241" height="480" viewBox="0 0 241 480">
    <polygon points="60,342 241,331 241,359" fill="var(--grey)"/>
    <polygon points="0,340 241,359 241,480 0,480" fill="var(--orange)"/>
  </svg>
  <h2 class="abs contact-title">Kontakt</h2>
  <svg class="contact-icon" style="left:12px;top:395px" width="14" height="13" viewBox="0 0 14 13" fill="none" stroke="#fff" stroke-width="1">
    <path d="M7 8 C4 5 4 2 7 1.5 C10 2 10 5 7 8Z"/><circle cx="7" cy="4" r="1"/><path d="M3 7 L1 12 H13 L11 7"/>
  </svg>
  <p class="abs contact contact-address">Karl Ewald Lambrecht<br>Lindenweg 12<br>24000 Musterhausen</p>
  <svg class="contact-icon" style="left:123px;top:395px" width="12" height="12" viewBox="0 0 12 12" fill="none" stroke="#fff" stroke-width="1">
    <path d="M2 1 L4 1 L5 4 L3.5 5 C4.5 7 5 7.5 7 8.5 L8 7 L11 8 L11 10 C11 11 10 11 9 11 C5 10.5 1.5 7 1 3 C1 2 1 1 2 1Z"/>
  </svg>
  <p class="abs contact contact-phone">04321 555019</p>
  <svg class="contact-icon" style="left:122px;top:423px" width="13" height="9" viewBox="0 0 13 9" fill="none" stroke="#fff" stroke-width="1">
    <rect x=".5" y=".5" width="12" height="8"/><path d="M.5 .5 L6.5 5 L12.5 .5"/>
  </svg>
  <p class="abs contact contact-mail">info@praxis-lambrecht-demo.de</p>
  <svg class="contact-icon" style="left:48px;top:444px" width="14" height="14" viewBox="0 0 14 14" fill="none" stroke="#fff" stroke-width="1">
    <rect x=".5" y="2" width="13" height="11.5" rx="1"/><path d="M.5 5 H13.5 M4 .5 V3 M10 .5 V3"/>
    <path d="M3 7.5 H4 M6.5 7.5 H7.5 M10 7.5 H11 M3 10.5 H4 M6.5 10.5 H7.5 M10 10.5 H11"/>
  </svg>
  <p class="abs contact contact-hours">Öffnungszeiten nach Absprache!</p>
</section>
<div class="panel-label" style="left:73px">Rückseite (2)</div>

<!-- Cover -->
<section class="panel panel--cover">
  <span class="abs brand-dot"></span>
  <h1 class="abs brand-name">KARL EWALD LAMBRECHT</h1>
  <p class="abs brand-tagline">Psychologische Beratung &amp; Therapie</p>
  <svg class="abs cover-art" width="241" height="480" viewBox="0 0 241 480">
    <defs>
      <linearGradient id="coverScene" x1="0" y1="0" x2="0" y2="1">
        <stop offset="0" stop-color="#b9c9d8"/>
        <stop offset=".35" stop-color="#dfe4e6"/>
        <stop offset=".55" stop-color="#8d9563"/>
        <stop offset=".8" stop-color="#8b7d68"/>
        <stop offset="1" stop-color="#6f6553"/>
      </linearGradient>
    </defs>
    <polygon points="0,66 241,82 241,90 0,76" fill="var(--grey)"/>
    <polygon points="92,74 241,70 241,88" fill="var(--orange)"/>
    <polygon points="0,76 241,89 241,480 0,480" fill="url(#coverScene)" role="img" aria-label="Foto: Holztreppe durch die Dünen hinauf zu einem Leuchtturm unter bewölktem Himmel"/>
  </svg>
</section>
<div class="panel-label" style="left:314px">Cover (1)</div>

<!-- Innenteil links -->
<section class="panel panel--inner-left">
  <svg class="abs portrait" width="241" height="480" viewBox="0 0 241 480">
    <defs>
      <linearGradient id="portraitTone" x1="0" y1="0" x2="1" y2="1">
        <stop offset="0" stop-color="#e9ecef"/>
        <stop offset=".5" stop-color="#c9b9a8"/>
        <stop offset="1" stop-color="#9fb3cc"/>
      </linearGradient>
    </defs>
    <path d="M118 0 A84 84 0 0 1 152 76" fill="none" stroke="var(--orange)" stroke-width="5"/>
    <path d="M0 160 A84 84 0 0 0 62 170" fill="none" stroke="var(--grey)" stroke-width="4"/>
    <circle cx="74" cy="86" r="82" fill="url(#portraitTone)" role="img" aria-label="Porträtfoto des Therapeuten"/>
  </svg>
  <p class="abs quote">„Bei aller Ernsthaftigkeit<br>und Empathie dürfen<br>Leichtigkeit, Zuversicht und<br>Humor in der Beratung<br>nicht zu kurz kommen.“</p>
  <span class="abs intro-bar"></span>
  <p class="abs intro-text">Mein Name ist Karl Ewald Lambrecht, ich bin Transaktionsanalytiker, psychotherapeutischer Heilpraktiker, begeisterter VKT®-Therapeut und Puppen-Comedian. Vielleicht ist es mir deshalb so wichtig, dass bei aller Ernsthaftigkeit und Empathie auch Zuversicht, Leichtigkeit und Humor im therapeutischen Prozess nicht zu kurz kommen sollten.<br>Meine Arbeit unterliegt supervisorischer Begleitung. Ich bin den Ethik-Richtlinien des Fachverbands für Transaktionsanalyse (FVTA) verpflichtet. Näheres dazu unter www.fvta-demo.de</p>
</section>
<div class="panel-label" style="left:646px">Innenteil (3)</div>

<!-- Innenteil rechts -->
<section class="panel panel--inner-right">
  <h2 class="abs services-title" style="font-weight:400">In diesen Bereichen kann<br>ich Sie unterstützen:</h2>

  <div class="service" style="top:82px">
    <svg class="service-icon" width="28" height="28" viewBox="0 0 28 28">
      <circle cx="14" cy="14" r="14" fill="var(--orange)"/>
      <circle cx="14" cy="9" r="3" fill="#fff"/>
      <path d="M8 20 C8 14 20 14 20 20Z" fill="#fff"/>
    </svg>
    <p class="service-name">Auftrittscoaching Mentales Training</p>
    <p class="service-text">Reduzieren Sie Ihre Präsentations- oder Prüfungsangst<br>und präsentieren Sie mit Lust und Freude.</p>
  </div>

  <div class="service" style="top:179px">
    <svg class="service-icon" width="28" height="28" viewBox="0 0 28 28">
      <circle cx="14" cy="14" r="14" fill="var(--orange)"/>
      <rect x="8" y="8" width="12" height="12" rx="1.5" fill="none" stroke="#fff" stroke-width="1.6"/>
      <path d="M14 11 V17 M11 14 H17" stroke="#fff" stroke-width="1.8"/>
    </svg>
    <p class="service-name">Entlastung in akuten Krisen</p>
    <p class="service-text">Zur Überbrückung der Wartezeit für eine kassenfinanzierte<br>Psychotherapie biete ich Kurztherapie zur Entlastung.</p>
  </div>

  <div class="service" style="top:276px">
    <svg class="service-icon" width="28" height="28" viewBox="0 0 28 28">
      <circle cx="14" cy="14" r="14" fill="var(--orange)"/>
      <circle cx="14" cy="10" r="3.5" fill="#fff"/>
      <path d="M7 21 C7 14.5 21 14.5 21 21Z" fill="#fff"/>
    </svg>
    <p class="service-name">Effektive Kurztherapie</p>
    <p class="service-text">Krisen, Ängste, geringes Selbstwertgefühl,<br>Depressionen: Hilfe für mehr Lebenszufriedenheit.</p>
  </div>

  <div class="service" style="top:376px">
    <svg class="service-icon" width="28" height="28" viewBox="0 0 28 28">
      <circle cx="14" cy="14" r="14" fill="var(--orange)"/>
      <circle cx="11" cy="10" r="2.8" fill="#fff"/>
      <circle cx="17.5" cy="11" r="2.5" fill="#fff"/>
      <path d="M6 20 C6 14.5 16 14.5 16 20Z M15 20 C15 15.5 22 15.5 22 20Z" fill="#fff"/>
    </svg>
    <p class="service-name">Coaching zu beruflichen Anliegen</p>
    <p class="service-text">Ich begleite Sie dabei, beruflich zufriedener und<br>erfolgreicher zu werden.</p>
  </div>
</section>
<div class="panel-label" style="left:886px">Innenteil (4)</div>

</body>
</html>
```